Boutique town planning business needs a Business Card design

We need a business card design for a new company called The Zoning Bridgeway. We provide town planning and urban design services to government, business and community groups. We would like to see the designs use the colours in the logo (blue, deep red, green and amber), plenty of white and including black and grey in the writing. The final design should communicate collaboration, creativity and professionalism and that we are approachable.

```html
<!DOCTYPE html>
<html lang="en">
<head>
<meta charset="utf-8">
<title>The Zoning Bridgeway – Business Card</title>
<link href="https://fonts.googleapis.com/css2?family=Open+Sans:wght@400;600;700&display=swap" rel="stylesheet">
<style>
  :root {
    --bg: #e9e6e1;
    --card-white: #fbfbfb;
    --card-black: #141414;
    --ink-dark: #3a3a3a;
    --ink-grey: #6f6f6f;
    --accent-blue: #2fb5d3;
    --accent-amber: #f4b320;
    --band-dark: #1c1c1c;
    --white: #ffffff;
  }
  * { margin: 0; padding: 0; box-sizing: border-box; }
  html, body { width: 1200px; height: 1023px; overflow: hidden; }
  body {
    background: var(--bg);
    font-family: "Open Sans", Arial, sans-serif;
    position: relative;
  }
  .card {
    position: absolute;
    left: 250px;
    width: 700px;
    height: 400px;
    border-radius: 4px;
    box-shadow: 0 10px 30px rgba(0,0,0,0.18);
    overflow: hidden;
  }
  .card--front { top: 90px; background: var(--card-white); }
  .card--back { top: 533px; background: var(--card-black); }

  .brand-mark {
    border-radius: 50%;
    background: var(--accent-blue);
    flex: none;
  }
  .brand-name {
    font-weight: 700;
    line-height: 1.05;
    letter-spacing: -0.5px;
  }

  .card--front .brand-mark {
    position: absolute;
    left: 48px; top: 44px;
    width: 120px; height: 120px;
  }
  .card--front .brand-name {
    position: absolute;
    left: 48px; top: 196px;
    font-size: 40px;
    color: var(--ink-dark);
  }

  .contact-block {
    position: absolute;
    right: 48px;
    top: 40px;
    width: 360px;
    text-align: right;
  }
  .person__name {
    color: var(--accent-blue);
    font-weight: 700;
    font-size: 19px;
    letter-spacing: 0.5px;
    text-transform: uppercase;
  }
  .person__credentials {
    color: var(--ink-grey);
    font-size: 12px;
    margin-top: 6px;
  }
  .person__role {
    color: var(--ink-grey);
    font-size: 12px;
    margin-top: 2px;
  }
  .contact-list {
    list-style: none;
    margin-top: 34px;
    display: inline-block;
    text-align: left;
  }
  .contact-list__item {
    display: flex;
    align-items: center;
    gap: 10px;
    color: var(--ink-dark);
    font-size: 13px;
    margin-bottom: 8px;
  }
  .contact-list__icon {
    width: 16px; height: 16px;
    border-radius: 3px;
    background: var(--accent-amber);
    display: flex; align-items: center; justify-content: center;
    flex: none;
  }
  .contact-list__icon svg { width: 10px; height: 10px; }

  .abn-band {
    position: absolute;
    left: 0; right: 0; bottom: 0;
    height: 36px;
    background: var(--band-dark);
    display: flex;
    align-items: center;
    padding-left: 48px;
    color: var(--white);
    font-size: 12px;
    letter-spacing: 1px;
  }

  .card--back .brand {
    position: absolute;
    left: 50%; top: 50%;
    transform: translate(-50%, -50%);
    display: flex;
    align-items: center;
    gap: 36px;
  }
  .card--back .brand-mark { width: 130px; height: 130px; }
  .card--back .brand-name { font-size: 36px; color: var(--white); }
</style>
</head>
<body>

<section class="card card--front" aria-label="Business card front">
  <span class="brand-mark"></span>
  <p class="brand-name">The Zoning<br>Bridgeway</p>

  <div class="contact-block">
    <p class="person__name">Maren Holloway</p>
    <p class="person__credentials">BTP (Town Planning), MUrbDes, Cert. Planner</p>
    <p class="person__role">Director</p>

    <ul class="contact-list">
      <li class="contact-list__item">
        <span class="contact-list__icon">
          <svg viewBox="0 0 10 10"><path d="M2 1h2l1 2-1.2 1a5 5 0 0 0 2.2 2.2L7 5l2 1v2a1 1 0 0 1-1 1A7 7 0 0 1 1 2a1 1 0 0 1 1-1z" fill="#fff"/></svg>
        </span>
        0400 318 257
      </li>
      <li class="contact-list__item">
        <span class="contact-list__icon">
          <svg viewBox="0 0 10 10"><rect x="1" y="2.5" width="8" height="5" fill="none" stroke="#fff" stroke-width="1"/><path d="M1 2.5l4 3 4-3" fill="none" stroke="#fff" stroke-width="1"/></svg>
        </span>
        hello@zoningbridgeway.com.au
      </li>
      <li class="contact-list__item">
        <span class="contact-list__icon">
          <svg viewBox="0 0 10 10"><circle cx="5" cy="5" r="3.6" fill="none" stroke="#fff" stroke-width="1"/><path d="M1.4 5h7.2M5 1.4c-2 2.2-2 5 0 7.2M5 1.4c2 2.2 2 5 0 7.2" fill="none" stroke="#fff" stroke-width="0.8"/></svg>
        </span>
        www.zoningbridgeway.com.au
      </li>
    </ul>
  </div>

  <div class="abn-band">ABN 12604837215</div>
</section>

<section class="card card--back" aria-label="Business card back">
  <div class="brand">
    <p class="brand-name">The Zoning<br>Bridgeway</p>
    <span class="brand-mark"></span>
  </div>
</section>

</body>
</html>
```